product leaflet for the aviation industry

Hello,
please prepare a leaflet design in A4 format, double-sided. Technical data can be found in the "A4 - leaflet" file on the first page. The leaflet can be arranged freely, but please include all substantive content from the "A4 - leaflet" file (pages 2 and 3). The company logo can be found in the attachment. Some of the photos can be downloaded from: https://vendrimax.qpanel.pl/.
The company operates for the aviation industry, so there may be an airplane or an aircraft turbine in the background.
Thank you in advance!
Target Market(s)
factories producing aircraft turbines
Industry/Entity Type
air

```html
<!DOCTYPE html>
<html lang="en">
<head>
<meta charset="utf-8">
<title>Vendrimax – Technical Consumables for Aerospace</title>
<link rel="stylesheet" href="https://fonts.googleapis.com/css2?family=Oswald:wght@500;600&family=Roboto:ital,wght@0,400;0,500;0,700;1,400&display=swap">
<style>
:root{
  --bg:#eceef4;
  --paper:#ffffff;
  --blue:#2e56a6;
  --blue-deep:#2a4a98;
  --blue-bright:#1f7fd8;
  --orange:#f4a93a;
  --ink:#2a2a2a;
  --muted:#666a73;
  --footer:#141414;
  --line:#5a7cc4;
}
*{box-sizing:border-box;margin:0;padding:0}
html,body{width:1200px;height:1200px;overflow:hidden}
body{background:var(--bg);font-family:"Roboto",Arial,sans-serif;position:relative}
.page{position:absolute;top:207px;width:550px;height:771px;background:var(--paper);overflow:hidden;box-shadow:0 2px 8px rgba(0,0,0,.12)}
.page--front{left:40px}
.page--back{left:612px}
.abs{position:absolute}

/* brand */
.brand{left:30px;top:40px;width:210px;text-align:center}
.brand__mark{display:inline-block;width:14px;height:14px;border-radius:50%;background:var(--blue);vertical-align:middle;margin-right:8px}
.brand__name{font-family:"Roboto",sans-serif;font-weight:700;font-size:28px;color:var(--blue);letter-spacing:1px;vertical-align:middle}

/* title */
.title-stripe{left:268px;top:14px;width:290px;height:104px;background:var(--blue);clip-path:polygon(22% 0,100% 0,100% 100%,0 100%)}
.title-panel{left:290px;top:14px;width:260px;height:104px;background:var(--orange);clip-path:polygon(20% 0,100% 0,100% 100%,0 100%)}
.title-panel h1{position:absolute;right:42px;top:10px;text-align:right;font-family:"Oswald",sans-serif;font-weight:500;font-size:27px;line-height:29px;color:#fff}

/* hero */
.hero-photo{left:230px;top:118px;width:320px;height:182px;background:linear-gradient(160deg,#6d90c8 0%,#c9b7a2 45%,#e89b52 62%,#4e5668 100%)}
.intro{left:0;top:118px;width:270px;height:182px;background:var(--blue-deep);clip-path:polygon(0 0,100% 0,88% 100%,0 100%);padding:16px 40px 0 18px;color:#fff;font-size:10px;line-height:12.3px}
.intro p+p{margin-top:11px}

/* section bands */
.band{height:30px;background:var(--blue-bright);color:#fff;font-family:"Oswald",sans-serif;font-weight:500;font-size:21px;line-height:30px;padding-left:36px;white-space:nowrap}
.band::after{content:"";position:absolute;right:-14px;top:0;width:8px;height:100%;background:var(--orange);transform:skewX(-20deg)}
.band::before{content:"";position:absolute;right:-4px;top:0;width:8px;height:100%;background:var(--blue-bright);transform:skewX(-20deg)}

/* cards */
.card{position:absolute}
.card__box{position:absolute;left:30px;top:0;right:0;bottom:0;border:1.2px solid var(--line);border-radius:6px;padding:6px 7px 0 33px;background:#fff}
.card__title{font-size:10px;font-weight:500;color:var(--blue);line-height:11.5px;margin-bottom:4px}
.card__text{font-size:6.6px;font-style:italic;color:var(--muted);line-height:8px;text-align:justify}
.card__text--dense{font-size:6.3px;line-height:7.4px}
.card__ring{position:absolute;left:0;top:50%;width:58px;height:58px;margin-top:-29px;border-radius:50%;border:3px solid var(--orange);background:#fff;z-index:2;display:flex;align-items:center;justify-content:center}
.card__ring span{width:44px;height:44px;border-radius:50%;background:radial-gradient(circle at 40% 40%,#d9dce2,#8e949e)}

/* footer */
.footer{left:0;top:720px;width:550px;height:51px;background:var(--footer);color:#fff}
.footer__brand{left:18px;top:15px;font-weight:700;font-size:18px;letter-spacing:1px}
.footer__brand i{display:inline-block;width:10px;height:10px;border-radius:50%;background:var(--blue-bright);margin-right:6px}
.footer__line{left:152px;top:8px;font-size:8.5px;line-height:11px}
.footer__line b{font-weight:500;font-size:8.5px;display:block;margin-left:12px}
.footer__row{display:flex;align-items:center;gap:4px}
.footer__addr{left:262px;top:19px;font-size:8.5px;line-height:10.5px;display:flex;gap:5px}
.footer__web{left:382px;top:0;width:168px;height:51px;background:var(--blue);clip-path:polygon(12% 0,100% 0,100% 100%,0 100%);display:flex;align-items:center;gap:7px;padding-left:25px;font-size:9.5px;font-weight:500;white-space:nowrap}
svg.ico{flex:none}

/* back page */
.lab-photo{left:0;top:297px;width:218px;height:134px;background:linear-gradient(180deg,#e8ebef 0%,#b9c0c8 55%,#8b939c 100%)}
.lab-accent{left:178px;top:297px;width:40px;height:30px;background:var(--orange);clip-path:polygon(0 0,100% 0,100% 100%)}
.lab-accent--low{left:190px;top:395px;width:30px;height:36px;clip-path:polygon(100% 0,100% 100%,0 100%)}
.services-band{left:218px;top:349px;width:332px;height:82px;background:var(--blue-deep);color:#fff;font-size:10px;line-height:12.3px;padding:16px 40px 0 38px}
.services-title{left:295px;top:315px;font-family:"Oswald",sans-serif;font-weight:500;font-size:22px;color:var(--blue)}
.services-tag{left:382px;top:319px;width:168px;height:27px;background:var(--orange);clip-path:polygon(7% 0,100% 0,100% 100%,0 100%);color:#fff;font-family:"Oswald",sans-serif;font-size:16px;line-height:27px;padding-left:22px}
.customers-tag{left:420px;top:420px;width:130px;height:27px;background:var(--orange);clip-path:polygon(8% 0,100% 0,100% 100%,0 100%);color:#fff;font-family:"Oswald",sans-serif;font-size:17px;line-height:27px;padding-left:26px}
.customers-lead{left:0;top:452px;width:550px;text-align:center;font-size:9px;font-style:italic;color:var(--blue)}
.client-grid{left:24px;top:476px;width:504px;display:grid;grid-template-columns:repeat(5,1fr);gap:5px 17px}
.client{height:26px;border:1px solid #dfe2e8;border-radius:2px;box-shadow:0 1px 2px rgba(0,0,0,.1);display:flex;align-items:center;justify-content:center;font-size:9.5px;font-weight:700;color:var(--blue)}
.map{left:22px;top:556px;width:245px;height:110px;border-radius:4px;background:linear-gradient(180deg,#3b84d4 0%,#2f73c9 100%)}
.ask-tag{left:415px;top:543px;width:135px;height:25px;background:var(--blue-bright);color:#fff;font-size:12px;font-weight:500;line-height:25px;padding-left:14px}
.contact-panel{left:300px;top:568px;width:250px;height:133px;background:var(--blue-deep);clip-path:polygon(12% 0,100% 0,100% 100%,0 100%)}
.contact-card{left:335px;top:578px;width:192px;height:98px;background:#fff;border-radius:8px;text-align:center;padding-top:10px}
.contact-card__name{font-size:20px;font-weight:500;color:var(--blue-deep);line-height:22px}
.contact-card__role{font-size:12px;color:var(--ink);margin-bottom:10px}
.contact-card__info{font-size:10px;color:var(--ink);line-height:13px}
.where-tag{left:0;top:689px;width:147px;height:28px;background:var(--blue-deep);color:#fff;font-size:12px;font-weight:500;line-height:28px;padding-left:24px}
.where-note{left:147px;top:689px;width:403px;height:28px;background:var(--blue-bright);color:#fff;font-size:8.2px;line-height:10.5px;padding:4px 0 0 15px}
.where-note em{font-style:normal;color:var(--orange)}
</style>
</head>
<body>

<section class="page page--front">
  <div class="abs brand"><span class="brand__mark"></span><span class="brand__name">VENDRIMAX</span></div>
  <div class="abs title-stripe"></div>
  <div class="abs title-panel"><h1>TECHNICAL<br>CONSUMABLES<br>FOR AEROSPACE</h1></div>

  <div class="abs hero-photo" role="img" aria-label="Business jet engine close-up on a runway at sunset"></div>
  <div class="abs intro">
    <p>Vendrimax specializes in manufacturing, spare parts details &amp; consumable materials used in special processes such as thermal spraying, hardfacing, brazing, welding, chemical processing, and more. We also produce tooling for testing aerospace materials and coatings.</p>
    <p>Our primary customers include manufacturers of new engine components &amp; maintenance, repair, and overhaul (MRO) facilities worldwide. Our production facility is AS9100 certified, and we hold a military license.</p>
  </div>

  <div class="abs band" style="left:0;top:309px;width:376px">CONSUMABLES FOR SPECIAL PROCESSES</div>

  <div class="card" style="left:20px;top:349px;width:245px;height:86px">
    <div class="card__ring" role="img" aria-label="Test coupons and substrates"><span></span></div>
    <div class="card__box">
      <div class="card__title">Coupons &amp; Substrates Machining</div>
      <p class="card__text">We specialize in manufacturing high-quality test coupons, substrates, specimens, samples, buttons, panels, discs, and strips for thermal spray, cold spray, chemical processing &amp; welding applications in the aviation industry. Our range of materials includes nickel and cobalt-based superalloys, titanium, hardened steel, and single crystals.</p>
    </div>
  </div>
  <div class="card" style="left:283px;top:349px;width:244px;height:86px">
    <div class="card__ring" role="img" aria-label="Regenerated coupons"><span></span></div>
    <div class="card__box">
      <div class="card__title">Coupons regeneration</div>
      <p class="card__text">Our regeneration service restores coated coupons to their original specifications. By using mechanical stripping processes, we offer a faster and more cost-effective alternative to producing new coupons. This results in significant savings on raw materials and heat treatment, while also reducing waste.</p>
    </div>
  </div>

  <div class="card" style="left:20px;top:442px;width:245px;height:86px">
    <div class="card__ring" role="img" aria-label="Green silicone masking ring"><span></span></div>
    <div class="card__box">
      <div class="card__title">Reusable Silicone Masking<br>/Hard Masking</div>
      <p class="card__text">Vendrimax's reusable silicone masking improves productivity and reduces costs by providing precise, durable protection for aero and gas turbine engine parts during processes such as thermal spray, grit blasting, shot peening, chemical processing, and vibratory finishing.</p>
    </div>
  </div>
  <div class="card" style="left:283px;top:442px;width:244px;height:86px">
    <div class="card__ring" role="img" aria-label="Pre-sintered brazing preform"><span></span></div>
    <div class="card__box">
      <div class="card__title">Pre-Sintered Diffusion<br>Brazing Preforms (PSP)</div>
      <p class="card__text">Superalloy and brazing products for aero engines, ideal for high-temperature repairs and dimensional restoration, with low porosity and minimal shrinkage.</p>
    </div>
  </div>

  <div class="card" style="left:20px;top:535px;width:245px;height:86px">
    <div class="card__ring" role="img" aria-label="Fan blade leading edge patches"><span></span></div>
    <div class="card__box">
      <div class="card__title">Fan Blade Leading Edge Patches,<br>Custom Spare Metal Parts</div>
      <p class="card__text">Manufacturer of aerospace components and spare parts for turbine engines, offering a wide range of materials.</p>
    </div>
  </div>
  <div class="card" style="left:283px;top:535px;width:244px;height:86px">
    <div class="card__ring" role="img" aria-label="Honeycomb structure sample"><span></span></div>
    <div class="card__box">
      <div class="card__title">Honeycomb</div>
      <p class="card__text">Honeycomb structures, with or without embedded brazing material, tailored to customer specifications and available in various forms like segments and rings, offer reduced assembly time with tape application, while Vendrimax also provides additional surface treatments as a value-added service.</p>
    </div>
  </div>

  <div class="card" style="left:20px;top:627px;width:245px;height:86px">
    <div class="card__ring" role="img" aria-label="Honeycomb tack welding shims"><span></span></div>
    <div class="card__box">
      <div class="card__title">Honeycomb Tack Welding Shims</div>
      <p class="card__text">Our shims are precision-made with flat surfaces, eliminating issues like convex edges that cause scorching on contact points and honeycomb surfaces. They ensure reliable performance and solve problems related to improper shim contact in demanding applications.</p>
    </div>
  </div>
  <div class="card" style="left:283px;top:627px;width:244px;height:86px">
    <div class="card__ring" role="img" aria-label="Fanned set of feeler gauges"><span></span></div>
    <div class="card__box">
      <div class="card__title">Custom Feeler Gauges<br>Manufacturing</div>
      <p class="card__text">Thanks to our WEDM capabilities, we manufacture precise tooling for measuring thickness, gaps, and spacing, such as the 0.1 mm feeler gauge shown in the photo.</p>
    </div>
  </div>

  <footer class="abs footer">
    <div class="abs footer__brand"><i></i>VENDRIMAX</div>
    <div class="abs footer__line">
      <b>INTERNATIONAL LINE</b>
      <div class="footer__row"><svg class="ico" width="8" height="8" viewBox="0 0 24 24"><path fill="#f4a93a" d="M6.6 10.8a15 15 0 0 0 6.6 6.6l2.2-2.2c.3-.3.7-.4 1-.2 1.1.4 2.3.6 3.6.6.6 0 1 .4 1 1V20c0 .6-.4 1-1 1A17 17 0 0 1 3 4c0-.6.4-1 1-1h3.5c.6 0 1 .4 1 1 0 1.3.2 2.5.6 3.6.1.3 0 .7-.2 1z"/></svg>+48 500 100 200</div>
      <div class="footer__row"><svg class="ico" width="8" height="8" viewBox="0 0 24 24"><path fill="#f4a93a" d="M2 5h20v14H2zm2 2v.5l8 5 8-5V7z"/></svg>info@vendrimax.qpanel.pl</div>
    </div>
    <div class="abs footer__addr"><svg class="ico" width="9" height="11" viewBox="0 0 24 30"><path fill="#f4a93a" d="M12 0a10 10 0 0 0-10 10c0 7.5 10 20 10 20s10-12.5 10-20A10 10 0 0 0 12 0zm0 14a4 4 0 1 1 0-8 4 4 0 0 1 0 8z"/></svg><span>12 Brzozowa Street<br>05-950 Lindowo, Poland</span></div>
    <div class="abs footer__web"><svg class="ico" width="12" height="12" viewBox="0 0 24 24" fill="none" stroke="#fff" stroke-width="2"><circle cx="12" cy="12" r="10"/><path d="M2 12h20M12 2c3 3 3 17 0 20M12 2c-3 3-3 17 0 20"/></svg>VENDRIMAX.QPANEL.PL</div>
  </footer>
</section>

<section class="page page--back">
  <div class="abs band" style="left:0;top:0;width:222px;height:39px;line-height:39px;padding-left:16px;font-size:17px">MODERN AVIATION MATERIALS</div>

  <div class="card" style="left:20px;top:48px;width:227px;height:88px">
    <div class="card__ring" role="img" aria-label="Ceramic composite parts"><span></span></div>
    <div class="card__box">
      <div class="card__title">Ceramic Composites<br>(Sic-SiC CMC)</div>
      <p class="card__text">Vendrimax supplies CMC SiC-SiC materials and components for aerospace and R&amp;D, driven by the growing use of CMCs in high-temperature engine parts.</p>
    </div>
  </div>
  <div class="card" style="left:280px;top:48px;width:244px;height:88px">
    <div class="card__ring" role="img" aria-label="Stacked superalloy sheets"><span></span></div>
    <div class="card__box" style="padding-top:5px">
      <div class="card__title" style="margin-bottom:3px">Aerospace Nickel &amp; Cobalt Base<br>Superalloys, Titanium, Steel,<br>Aluminium Alloys</div>
      <p class="card__text card__text--dense">Vendrimax offers a comprehensive range of aerospace raw materials (wrought and cast), including Nicorel, Renox, single crystals, Haxley and many others. We are able to supply difficult to find raw materials in required shapes and dimensions.</p>
    </div>
  </div>

  <div class="abs band" style="left:0;top:145px;width:272px;height:34px;line-height:34px;padding-left:16px;font-size:17px">CONSUMABLES FOR AEROSPACE LABS</div>

  <div class="card" style="left:20px;top:189px;width:227px;height:86px">
    <div class="card__ring" role="img" aria-label="High-temperature metal pullrods"><span></span></div>
    <div class="card__box">
      <div class="card__title">High-temperature Custom<br>Metal Accessories</div>
      <p class="card__text">Custom accessories and high-temperature equipment, such as pullrods, couplings, fixtures, made of cast nickel superalloys, for creep, stress rupture and tensile testing at elevated temperatures up to 1300°C.</p>
    </div>
  </div>
  <div class="card" style="left:280px;top:189px;width:244px;height:86px">
    <div class="card__ring" role="img" aria-label="V-grooved curing fixture"><span></span></div>
    <div class="card__box">
      <div class="card__title">Coating Evaluation Laboratory<br>Accessories</div>
      <p class="card__text">Manufacturing of custom laboratory accessories including Gravity or pressure type V-grooved curing fixture for Tensile Bond Strength test of coating, Loading fixtures, concentricity gauge with dial indicator and more...</p>
    </div>
  </div>

  <div class="abs lab-photo" role="img" aria-label="Row of wire EDM machines in a workshop"></div>
  <div class="abs lab-accent"></div>
  <div class="abs lab-accent lab-accent--low"></div>
  <div class="abs services-title">SERVICES</div>
  <div class="abs services-tag">WIRE EDM (WEDM)</div>
  <div class="abs services-band">Our advanced WEDM technology allows cutting materials up to 700 mm thick, ensuring minimal thermal impact and the highest precision.</div>

  <div class="abs customers-tag">CUSTOMERS</div>
  <p class="abs customers-lead">Our experience &amp; commitment to quality has been recognized by leading aircraft engine manufacturers such as:</p>
  <div class="abs client-grid">
    <div class="client">Corvan Aero</div>
    <div class="client">Heltrix</div>
    <div class="client">Parlow Engines</div>
    <div class="client">Kestrane</div>
    <div class="client">Montar</div>
    <div class="client">Solvane</div>
    <div class="client">Erto</div>
    <div class="client">Linvora</div>
    <div class="client">Elmora</div>
    <div class="client">Greenfold</div>
  </div>

  <div class="abs map" role="img" aria-label="World map with office locations marked"></div>
  <div class="abs contact-panel"></div>
  <div class="abs ask-tag">ANY QUESTIONS?</div>
  <div class="abs contact-card">
    <div class="contact-card__name">Aldous Wren</div>
    <div class="contact-card__role">Sales Director</div>
    <div class="contact-card__info">+44 (0) 7700 90 04 12<br>aldous.wren@vendrimax.qpanel.pl</div>
  </div>
  <div class="abs where-tag">WHERE ARE WE?</div>
  <div class="abs where-note">We're available across 6 continents. Contact our Sales Director or reach us directly at <em>info@vendrimax.qpanel.pl</em>, and our headquarters will promptly handle your inquiry!</div>

  <footer class="abs footer">
    <div class="abs footer__brand"><i></i>VENDRIMAX</div>
    <div class="abs footer__line">
      <b>INTERNATIONAL LINE</b>
      <div class="footer__row"><svg class="ico" width="8" height="8" viewBox="0 0 24 24"><path fill="#f4a93a" d="M6.6 10.8a15 15 0 0 0 6.6 6.6l2.2-2.2c.3-.3.7-.4 1-.2 1.1.4 2.3.6 3.6.6.6 0 1 .4 1 1V20c0 .6-.4 1-1 1A17 17 0 0 1 3 4c0-.6.4-1 1-1h3.5c.6 0 1 .4 1 1 0 1.3.2 2.5.6 3.6.1.3 0 .7-.2 1z"/></svg>+48 500 100 200</div>
      <div class="footer__row"><svg class="ico" width="8" height="8" viewBox="0 0 24 24"><path fill="#f4a93a" d="M2 5h20v14H2zm2 2v.5l8 5 8-5V7z"/></svg>info@vendrimax.qpanel.pl</div>
    </div>
    <div class="abs footer__addr"><svg class="ico" width="9" height="11" viewBox="0 0 24 30"><path fill="#f4a93a" d="M12 0a10 10 0 0 0-10 10c0 7.5 10 20 10 20s10-12.5 10-20A10 10 0 0 0 12 0zm0 14a4 4 0 1 1 0-8 4 4 0 0 1 0 8z"/></svg><span>12 Brzozowa Street<br>05-950 Lindowo, Poland</span></div>
    <div class="abs footer__web"><svg class="ico" width="12" height="12" viewBox="0 0 24 24" fill="none" stroke="#fff" stroke-width="2"><circle cx="12" cy="12" r="10"/><path d="M2 12h20M12 2c3 3 3 17 0 20M12 2c-3 3-3 17 0 20"/></svg>VENDRIMAX.QPANEL.PL</div>
  </footer>
</section>

</body>
</html>
```